Building company buisness cards

We are looking for a sharp modern new look for our business cards.
We are a New Zealand based company that specialises in house and land packages.
We have attached a photo of the current logo and would like to see if it can be improved somehow if needed.
We are open to any colours but we have chosen green at this stage.
Feel free to change the font and make the logo smarter looking.
Play with the colours and see what looks best.

We want a card that looks so good know one will want to throw it away!

Target Market(s)

Home buyers

Industry/Entity Type

Building

Contact Information for Business Card

Dorian Keswick
0217392604
dkeswick@tidewellhomecraft.co.nz
tidewellhomecraft.co.nz

Font styles to use
Serif
Sans Serif

Colors

Designer to choose colors to be used in the design.

Requirements
Must have
• Logo and company name on one side, details on the other side
Nice to have
• Color codes for the original green are HEX #4a8028, RGB(74,128,40), CMYK(42,0,69,50)
• Round corners, Raised and/or spot UV

```html
<!DOCTYPE html>
<html lang="en">
<head>
<meta charset="utf-8">
<title>Tidewell Homecraft – Business Cards</title>
<link href="https://fonts.googleapis.com/css2?family=Montserrat:wght@800&family=Raleway:wght@300;400;600&display=swap" rel="stylesheet">
<style>
  :root {
    --stage: #222324;
    --brand-green: #4a8028;
    --card-green: #58913a;
    --logo-tint: #8fc06d;
    --paper: #ffffff;
    --ink-light: #f3f7ef;
    --rule-grey: #b9c2b3;
  }
  * { margin: 0; padding: 0; box-sizing: border-box; }
  html, body { width: 800px; height: 1200px; overflow: hidden; }
  body {
    background: var(--stage);
    font-family: "Raleway", sans-serif;
    position: relative;
  }
  .card {
    position: absolute;
    left: 80px;
    width: 640px;
    height: 370px;
    border-radius: 26px;
    overflow: hidden;
  }
  .card--front { top: 150px; background: var(--card-green); }
  .card--back { top: 680px; background: var(--paper); }

  .brand {
    position: absolute;
    left: 0; right: 0;
    display: flex;
    align-items: center;
    justify-content: center;
    gap: 14px;
  }
  .brand__mark {
    width: 22px; height: 22px;
    border-radius: 4px;
  }
  .brand__name {
    font-family: "Montserrat", sans-serif;
    font-weight: 800;
    font-size: 40px;
    letter-spacing: -0.5px;
    line-height: 1;
  }
  .card--front .brand { top: 92px; }
  .card--front .brand__mark { background: var(--logo-tint); }
  .card--front .brand__name { color: var(--logo-tint); }

  .divider {
    position: absolute;
    top: 196px;
    left: 0; right: 0;
    display: flex;
    align-items: center;
    gap: 14px;
    color: var(--ink-light);
  }
  .divider::before, .divider::after {
    content: "";
    flex: 1;
    height: 2px;
    background: var(--ink-light);
  }
  .holder-name {
    font-weight: 600;
    font-size: 22px;
    letter-spacing: 0.3px;
  }
  .contact {
    position: absolute;
    top: 240px;
    left: 0; right: 0;
    text-align: center;
    color: var(--ink-light);
    font-weight: 300;
    font-size: 16px;
    line-height: 1.7;
  }
  .contact b { font-weight: 600; font-style: italic; }

  .card--back .brand { top: 150px; }
  .card--back .brand__mark { background: var(--brand-green); }
  .card--back .brand__name { color: var(--brand-green); font-size: 46px; }
  .back-rule {
    position: absolute;
    top: 222px;
    left: 50%;
    width: 90px;
    margin-left: -45px;
    height: 1px;
    background: var(--rule-grey);
  }
</style>
</head>
<body>
  <section class="card card--front" aria-label="Card front">
    <div class="brand">
      <span class="brand__mark"></span>
      <span class="brand__name">tidewell homecraft</span>
    </div>
    <div class="divider"><span class="holder-name">Dorian Keswick</span></div>
    <div class="contact">
      <p><b>P:</b> 0217392604 | <b>E:</b> dkeswick@tidewellhomecraft.co.nz</p>
      <p>tidewellhomecraft.co.nz</p>
    </div>
  </section>

  <section class="card card--back" aria-label="Card back">
    <div class="brand">
      <span class="brand__mark"></span>
      <span class="brand__name">tidewell homecraft</span>
    </div>
    <div class="back-rule"></div>
  </section>
</body>
</html>
```